Business card design needed

I am a business consultant but I call myself an "organizational leadership consultant." My clients hire me to do organizational development work in the areas of leadership development, strategic planning, shared visioning, governance (bylaws, policy, board development), collaborative capacity building, and organizational communications. I work in numerous sectors (public, private, not-for-profit and governmental) but most of my clients are in not-for-profit (but not human service - think national advocacy organizations, student governments, regulatory colleges, and professional (accreditation) bodies).

I want my cards to convey the concepts of being reliable and smart (of course) but also vibrant and signifying new beginnings/possibilities.

I am uploading a copy of a logo I have used for some time (adapted from QX logo free website). I like the hues of the primary colours used, its symmetrical, and that it has movement. I am open to a new logo (but not essential) with these same qualities: I really like fractals BTW.

I think one of the most beautiful creatures on earth is the harlequin duck, but have not been able to figure out how to incorporate that into my brand. Mostly what I love is the colours and how they appear on the duck. I am sharing that just as an idea in case your creative energy is leaning toward creating a new design rather than working with my logo.

If I had the right business card to start with, I might consider re-branding and working that into my digital and print materials. I realize this is against the use of RGBY in my current logo.
Updates

Hi - I forgot to mention to please use the PVRA Certified patch/logo as a just a small feature of the card - it is not my main logo. Also, I like fonts that are clean.  Thanks!

Target Market(s)

Higher level business professionals

Industry/Entity Type

Business Consultant

Contact Information for Business Card

Corla Whitfield, MA, BSc, PVRA(pls insert trademark symbol)
Organizational Leadership Consultant
250-487-6019
corla@cwhitfieldadvisory.example
www.cwhitfieldadvisory.example
Fernbrook Cove, BC

Logo Text

Guiding Leaders Toward a Brighter Future

Logo styles of interest
Emblem Logo
Abstract Logo
Requirements
Must have
• Must have:
1. Name of my business (Corla Whitfield Consulting) and contact info per above
2. My logo (or your new idea for a logo) with a my tagline somewhere (tagline can be on back. Tagline is "Guiding Leaders Toward a Brighter Future)
3. PVRA certified logo (attachment #3)
3. Chirpora logo with my acct name (@corlawhitfield), and
4. Workvine logo
Should not have
• I don't like the "solid" primary colours as in those found on brikko or in a pebblies box - transparency in those colours is acceptable.

Do not include images of people shaking hands or other corny 'business' imagery.;-)

```html
<!DOCTYPE html>
<html lang="en">
<head>
<meta charset="utf-8">
<title>Corla Whitfield Consulting — Business Cards</title>
<link rel="stylesheet" href="https://fonts.googleapis.com/css2?family=Arimo:wght@400;700&family=Michroma&display=swap">
<style>
  :root {
    --backdrop: #e9e6e1;
    --card-white: #ffffff;
    --sky: #8ecff5;
    --mist: rgba(170, 220, 235, 0.55);
    --sun: rgba(248, 244, 170, 0.6);
    --ink: #1c1c1c;
    --text: #2b2b2b;
    --rust: #c2410c;
    --ember: #f26522;
    --leaf: #7cae3c;
    --ocean: #3a80b4;
    --gold: #e8ac10;
  }
  * { box-sizing: border-box; margin: 0; padding: 0; }
  html, body {
    width: 1000px; height: 1200px; overflow: hidden;
    background: var(--backdrop);
    font-family: "Arimo", Arial, sans-serif;
  }
  .sheet { position: relative; width: 1000px; height: 1200px; }

  .card {
    position: absolute; left: 185px; width: 645px; height: 405px;
    background: var(--card-white); overflow: hidden;
    box-shadow: 0 2px 6px rgba(0,0,0,0.18);
  }
  .card--front { top: 160px; }
  .card--back { top: 620px; }

  .wash {
    position: absolute; inset: 0;
    background:
      radial-gradient(ellipse 260px 200px at 20px 330px, var(--mist), transparent 70%),
      radial-gradient(ellipse 240px 140px at 330px 0px, rgba(190,230,245,0.5), transparent 70%),
      radial-gradient(ellipse 220px 260px at 640px 120px, var(--sun), transparent 70%),
      radial-gradient(ellipse 200px 140px at 420px 380px, rgba(250,246,190,0.55), transparent 70%);
  }
  .glass {
    position: absolute; border-radius: 22px;
    background: rgba(255,255,255,0.35);
    border: 1px solid rgba(255,255,255,0.6);
  }

  /* Front */
  .emblem {
    position: absolute; left: 225px; top: 68px; width: 200px; height: 200px;
    border-radius: 50%; background: var(--leaf); opacity: 0.85;
  }
  .wordmark {
    position: absolute; left: 0; right: 0; top: 291px; text-align: center;
    font-size: 23px; font-weight: 400; color: var(--ink); letter-spacing: -0.2px;
  }
  .tagline {
    position: absolute; left: 0; right: 0; top: 315px; text-align: center;
    font-size: 9px; color: var(--rust); letter-spacing: 1.4px;
    text-transform: uppercase;
  }
  .url-band {
    position: absolute; left: 0; right: 0; bottom: 0; height: 29px;
    background: var(--sky); color: #fff; text-align: center;
    font-family: "Michroma", "Arimo", sans-serif; font-size: 13px;
    letter-spacing: 2.6px; line-height: 29px; text-transform: uppercase;
  }

  /* Back */
  .cert-badge {
    position: absolute; left: 37px; top: 30px; width: 86px; height: 86px;
    border-radius: 14px; background: var(--ember);
  }
  .corner-mark {
    position: absolute; left: 520px; top: 75px; width: 250px; height: 250px;
    border-radius: 50%;
    background: radial-gradient(circle at 35% 55%, rgba(58,128,180,0.85), rgba(124,174,60,0.8) 60%, rgba(232,172,16,0.75));
  }
  .identity { position: absolute; left: 75px; top: 235px; }
  .identity__name {
    display: inline-block;
    font-size: 20px; font-weight: 700; color: var(--ink); line-height: 22px;
  }
  .identity__firm {
    display: block; text-align: right; margin-top: -4px;
    font-size: 7px; font-weight: 400; line-height: 8px;
    color: var(--ember); letter-spacing: 1px; text-transform: uppercase;
  }
  .identity__details {
    list-style: none; margin: 5px 0 0 12px;
    font-size: 11px; line-height: 16px; color: var(--text);
  }
  .identity__details sup { font-size: 6px; }
  .contact {
    position: absolute; left: 420px; top: 318px; list-style: none;
    font-size: 10.5px; line-height: 17px; color: var(--text);
  }
  .contact b { color: var(--ink); }
  .bar { position: absolute; bottom: 0; height: 22px; }
  .bar--leaf { left: 0; width: 413px; background: var(--leaf); }
  .bar--ocean { left: 418px; right: 0; background: var(--ocean); }
</style>
</head>
<body>
<main class="sheet">
  <section class="card card--front" aria-label="Card front">
    <div class="wash"></div>
    <div class="glass" style="left:15px; top:290px; width:160px; height:140px;"></div>
    <div class="glass" style="left:470px; top:40px; width:200px; height:300px;"></div>
    <div class="emblem" aria-hidden="true"></div>
    <h1 class="wordmark">Corla Whitfield Consulting</h1>
    <p class="tagline">Guiding Leaders Toward a Brighter Future</p>
    <p class="url-band">www.cwhitfieldadvisory.example</p>
  </section>

  <section class="card card--back" aria-label="Card back">
    <div class="wash"></div>
    <div class="glass" style="left:15px; top:130px; width:100px; height:185px;"></div>
    <div class="glass" style="left:330px; top:35px; width:190px; height:260px;"></div>
    <div class="cert-badge" aria-hidden="true"></div>
    <div class="corner-mark" aria-hidden="true"></div>
    <div class="identity">
      <h2 class="identity__name">Corla Whitfield<span class="identity__firm">Consulting</span></h2>
      <ul class="identity__details">
        <li>MA, BSc, PVRA<sup>®</sup></li>
        <li>Organizational Leadership Consultant</li>
        <li>Fernbrook Cove, BC</li>
      </ul>
    </div>
    <ul class="contact">
      <li><b>Phone:</b> 250-487-6019</li>
      <li><b>Email:</b> corla@cwhitfieldadvisory.example</li>
      <li><b>Site:</b> www.cwhitfieldadvisory.example</li>
    </ul>
    <div class="bar bar--leaf"></div>
    <div class="bar bar--ocean"></div>
  </section>
</main>
</body>
</html>
```